Design My Bussiness Card
Technology company
Project: Design My Bussiness Card
Design My Bussiness Card -
Creative Brief
Professional
Dorian Pelkey
2847 E. Tollbrook #3
marisa@vantrelo.net
www.qoribelix.info

```html
<!DOCTYPE html>
<html lang="en">
<head>
<meta charset="utf-8">
<title>Qoribelix Stationery</title>
<link rel="stylesheet" href="https://fonts.googleapis.com/css2?family=Cinzel:wght@600&family=Tinos:wght@400;700&display=swap">
<style>
:root{
  --stage:#4a4a4a;
  --paper:#ffffff;
  --green:#2f9a3c;
  --green-dark:#1c7a2c;
  --green-light:#4cc25a;
  --brown:#3b2a22;
  --ink:#2b2b2b;
}
*{margin:0;padding:0;box-sizing:border-box}
html,body{width:1200px;height:919px;overflow:hidden;background:var(--stage)}
.canvas{position:relative;width:1200px;height:919px;font-family:"Tinos",serif;color:var(--ink)}
.piece{position:absolute;background:var(--paper);box-shadow:0 2px 6px rgba(0,0,0,.35)}
.brand{position:absolute;display:flex;align-items:center;gap:8px}
.brand-dot{border-radius:50%;background:var(--green);flex:none}
.brand-name{font-family:"Cinzel",serif;font-weight:600;color:var(--green-dark);line-height:1;white-space:nowrap}
.tagline{position:absolute;font-family:"Tinos",serif;color:var(--green);text-transform:uppercase;letter-spacing:.5px;white-space:nowrap}
.contact{position:absolute;font-size:11px;line-height:15px;white-space:nowrap}
.contact span{display:block}
.contact span::before{content:"";display:inline-block;width:6px;height:6px;background:var(--green);margin-right:5px;vertical-align:middle}

/* letterhead */
.letterhead{left:169px;top:37px;width:502px;height:800px;border-bottom:6px solid var(--brown)}
.letterhead .brand{left:22px;top:22px}
.letterhead .brand-dot{width:28px;height:28px}
.letterhead .brand-name{font-size:24px}
.letterhead .tagline{left:58px;top:58px;font-size:8px}
.letterhead .contact{left:352px;top:26px;font-size:9px;line-height:12px}
.letterhead .contact.col2{left:412px}

/* business card front */
.card-front{left:117px;top:181px;width:219px;height:134px;border-radius:12px}
.card-front .brand{left:12px;top:12px;gap:5px}
.card-front .brand-dot{width:16px;height:16px}
.card-front .brand-name{font-size:14px}
.card-front .tagline{left:33px;top:32px;font-size:5px}
.card-front .holder{position:absolute;left:14px;top:76px;font-size:10px;font-weight:700}
.card-front .contact{left:14px;top:91px;font-size:6px;line-height:8px}
.card-front .contact.col2{left:80px}
.card-front .contact span::before{width:4px;height:4px;margin-right:3px}

/* business card back */
.card-back{left:35px;top:355px;width:233px;height:132px;border-radius:12px;background:linear-gradient(135deg,var(--green-light),var(--green) 55%,var(--green-dark))}
.card-back .brand{left:22px;top:46px;gap:6px}
.card-back .brand-dot{width:22px;height:22px;background:var(--paper)}
.card-back .brand-name{font-size:20px;color:var(--paper)}
.card-back .tagline{left:50px;top:72px;font-size:6px;color:var(--paper)}

/* envelope back */
.envelope-back{left:455px;top:127px;width:564px;height:365px}
.envelope-back .flap{position:absolute;left:0;top:0;width:100%;height:67px;background:linear-gradient(180deg,var(--green-light),var(--green))}
.envelope-back .flap-name{position:absolute;right:26px;top:26px;font-family:"Cinzel",serif;font-weight:600;font-size:14px;color:var(--green-dark)}
.envelope-back .brand{left:20px;top:80px}
.envelope-back .brand-dot{width:30px;height:30px}
.envelope-back .brand-name{font-size:26px}
.envelope-back .tagline{left:58px;top:118px;font-size:9px}

/* envelope front */
.envelope-front{left:343px;top:447px;width:695px;height:256px;border-left:12px solid var(--brown)}
.envelope-front .brand{left:14px;top:-26px;margin-top:50px}
.envelope-front .brand-dot{width:32px;height:32px}
.envelope-front .brand-name{font-size:28px}
.envelope-front .tagline{left:54px;top:64px;font-size:9px}
.envelope-front .contact{left:14px;top:192px}
.envelope-front .contact.col2{left:110px}
.envelope-front .side-brand{position:absolute;right:-34px;top:118px;transform:rotate(-90deg);display:flex;align-items:center;gap:6px}
.envelope-front .side-brand .brand-dot{width:18px;height:18px}
.envelope-front .side-brand .brand-name{font-size:16px}
</style>
</head>
<body>
<main class="canvas">

  <section class="piece letterhead" aria-label="Letterhead">
    <div class="brand"><span class="brand-dot"></span><span class="brand-name">Qoribelix</span></div>
    <div class="tagline">Professional Business Services</div>
    <div class="contact"><span>5550143827</span><span>5550143827</span><span>2847 E. Tollbrook #3</span></div>
    <div class="contact col2"><span>marisa@vantrelo.net</span><span>www.qoribelix.info</span></div>
  </section>

  <section class="piece envelope-back" aria-label="Envelope back">
    <div class="flap"><span class="flap-name">Qoribelix</span></div>
    <div class="brand"><span class="brand-dot"></span><span class="brand-name">Qoribelix</span></div>
    <div class="tagline">Professional Business Services</div>
  </section>

  <section class="piece card-front" aria-label="Business card front">
    <div class="brand"><span class="brand-dot"></span><span class="brand-name">Qoribelix</span></div>
    <div class="tagline">Professional Business Services</div>
    <div class="holder">Dorian Pelkey</div>
    <div class="contact"><span>5550143827</span><span>5550143827</span><span>2847 E. Tollbrook #3</span></div>
    <div class="contact col2"><span>marisa@vantrelo.net</span><span>www.qoribelix.info</span></div>
  </section>

  <section class="piece card-back" aria-label="Business card back">
    <div class="brand"><span class="brand-dot"></span><span class="brand-name">Qoribelix</span></div>
    <div class="tagline">Professional Business Services</div>
  </section>

  <section class="piece envelope-front" aria-label="Envelope front">
    <div class="brand"><span class="brand-dot"></span><span class="brand-name">Qoribelix</span></div>
    <div class="tagline">Professional Business Services</div>
    <div class="contact"><span>5550143827</span><span>5550143827</span><span>2847 E. Tollbrook #3</span></div>
    <div class="contact col2"><span>marisa@vantrelo.net</span><span>www.qoribelix.info</span></div>
    <div class="side-brand"><span class="brand-dot"></span><span class="brand-name">Qoribelix</span></div>
  </section>

</main>
</body>
</html>
```